Bright Meadow LLC business card

I help with the Marketing and Sales of various Natural, Organic, Eco Friendly and Healthy Main Stream products to Retail Corporate accounts as well as Independents and Distributors.I also highlight Private label items to these same Retail Corporate accounts.Cherish the Moments, Enjoy Life!

Speciality & Health Sales and Marketing

Target Market(s)

Men and Women

Industry/Entity Type

Business

Contact Information for Business Card

Bright Meadow, LLC
Janet Lou Brindall
418 West Fern Lane
Ste 3-274
Phoenix, AZ 85047
602-555-0173
jbrindall@veltramail.net

Requirements
Must have
• Nice, femine font
Something in the background or on a side with a softness
Nice to have
• Cherish the Moments, Enjoy Life
Should not have
• Hardness

```html
<!DOCTYPE html>
<html lang="en">
<head>
<meta charset="utf-8">
<title>Bright Meadow LLC – Business Card</title>
<link rel="stylesheet" href="https://fonts.googleapis.com/css2?family=Satisfy&family=Dancing+Script:wght@400&family=Quicksand:wght@500&display=block">
<style>
  :root {
    --stage: #4b4a5a;
    --card-light: #f8c3da;
    --card-mid: #f3a9c9;
    --card-deep: #ec8cb8;
    --band: #f7cfe0;
    --band-edge: #fde6ef;
    --bloom: rgba(255, 255, 255, 0.16);
    --text: #ffffff;
    --icon: #e8358a;
  }
  * { margin: 0; padding: 0; box-sizing: border-box; }
  html, body {
    width: 1200px;
    height: 900px;
    overflow: hidden;
    background: var(--stage);
  }
  .business-card {
    position: absolute;
    left: 150px;
    top: 179px;
    width: 900px;
    height: 541px;
    overflow: hidden;
    background: linear-gradient(160deg, var(--card-light) 0%, var(--card-mid) 55%, var(--card-deep) 100%);
  }
  .soft-bloom {
    position: absolute;
    left: 300px;
    top: 0;
    width: 600px;
    height: 541px;
    background: radial-gradient(ellipse at 75% 55%, var(--bloom) 0%, rgba(255,255,255,0.06) 45%, rgba(255,255,255,0) 75%);
  }
  .lace-band {
    position: absolute;
    left: 88px;
    top: 0;
    width: 212px;
    height: 541px;
    background: linear-gradient(180deg, var(--band) 0%, #f4c0d7 50%, var(--band) 100%);
    border-left: 4px double var(--band-edge);
    border-right: 4px double var(--band-edge);
  }
  .tagline {
    position: absolute;
    left: 349px;
    top: 78px;
    width: 520px;
    font-family: "Satisfy", "Dancing Script", cursive;
    font-weight: 400;
    font-style: normal;
    font-size: 48px;
    line-height: 60px;
    color: var(--text);
    white-space: nowrap;
  }
  .tagline .line { display: block; }
  .tagline .line-first { width: 520px; }
  .tagline .line-second { padding-left: 230px; }
  .contact {
    position: absolute;
    left: 319px;
    top: 286px;
    font-family: "Quicksand", sans-serif;
    font-weight: 500;
    font-size: 20px;
    color: var(--text);
    list-style: none;
    white-space: nowrap;
  }
  .contact-item {
    display: flex;
    align-items: flex-start;
    margin-bottom: 14px;
    line-height: 27px;
  }
  .contact-icon {
    flex: 0 0 auto;
    width: 30px;
    height: 27px;
    margin-right: 7px;
  }
  .contact-item.address { margin-top: -10px; }
  .contact-item.address .contact-icon { margin-top: 38px; }
  .contact-address { font-style: normal; }
</style>
</head>
<body>
  <main class="business-card">
    <div class="soft-bloom" role="img" aria-label="Faint large floral ornament in the card background"></div>
    <div class="lace-band" role="img" aria-label="Vertical white lace band with mandala flower pattern"></div>

    <h1 class="tagline">
      <span class="line line-first">Cherish the Moments,</span>
      <span class="line line-second">Enjoy Life!</span>
    </h1>

    <ul class="contact">
      <li class="contact-item phone">
        <svg class="contact-icon" viewBox="0 0 30 27" aria-hidden="true">
          <path d="M6 4 C4 6 4 10 7 14 C10 19 15 23 19 24 C22 25 24 23 25 21 L21 17 L18 19 C15 18 11 14 10 11 L12 8 Z" fill="none" stroke="var(--icon)" stroke-width="2.4" stroke-linejoin="round"/>
        </svg>
        <span>602-555-0173</span>
      </li>
      <li class="contact-item email">
        <svg class="contact-icon" viewBox="0 0 30 27" aria-hidden="true">
          <rect x="2" y="6" width="26" height="16" fill="none" stroke="var(--icon)" stroke-width="2.2"/>
          <path d="M2 6 L15 15 L28 6" fill="none" stroke="var(--icon)" stroke-width="2.2"/>
        </svg>
        <span>jbrindall@veltramail.net</span>
      </li>
      <li class="contact-item address">
        <svg class="contact-icon" viewBox="0 0 30 27" aria-hidden="true">
          <path d="M15 25 C10 19 7 15 7 10 A8 8 0 0 1 23 10 C23 15 20 19 15 25 Z" fill="none" stroke="var(--icon)" stroke-width="2.2"/>
          <circle cx="15" cy="10" r="3" fill="none" stroke="var(--icon)" stroke-width="2"/>
        </svg>
        <address class="contact-address">
          Bright Meadow,<br>
          LLC Janet Lou Brindall 418<br>
          West Fern Lane<br>
          Ste 3-274 Phoenix, AZ 85047
        </address>
      </li>
    </ul>
  </main>
</body>
</html>
```